New Massage Business needs a Card design

We need a card design for our new massage therapy business based in Sydney, Au. The business is getting a makeover, so a little later on we'll need shirts, various pamphlets and promotional flyers, and possibly a website. The winner will be offered those jobs as well.

Colour scheme should be green, black, and steel/charcoal grey. The business focuses on massage as an anatomical solution to stress, muscle aches, pains and fatigue. Ideally we'd like an anatomical image of the muscle system (ref to the attached files). In my mind this image takes up most of the left third of the card, and shows points of tension and pain at the neck and lower back. This image should be the grey portion of the card.

On the upper right is the other image attached, with a simple line drawing of a vehicle on the left end of the line, and a building on the right end replacing the stick figure (we have a therapist specializing in mobile massage). The blank part in the middle of the line should have "Kestrel Wellness", and in smaller writing below, "The Tension Fix".

Bottom right corner should have the contact and business details.
On the back we'd like a "next appointment" and "refer a friend" option.

If you have a design which doesn't fit the above, but you feel suits the business, please submit anyway - sometimes you don't know what you like until you see it.

Business Details:
Name: Kestrel Wellness - The Tension Fix

Industry/Entity Type

Massage Therapy

Contact Information for Business Card

Business Details:
Contact name: Marcus
Title: Massage Therapist
Contact: 0458203617
Email: info@ktfbodywork.example

Requirements
Must have
• Colour scheme should be green, black, and steel/charcoal grey. The business focuses on massage as an anatomical solution to stress, muscle aches, pains and fatigue. Ideally we'd like an anatomical image of the muscle system (ref to the attached files). In my mind this image takes up most of the left third of the card, and shows points of tension and pain at the neck and lower back. This image should be the grey portion of the card.
• On the upper right is the other image attached, with a simple line drawing of a vehicle on the left end of the line, and a building on the right end replacing the stick figure (we have a therapist specializing in mobile massage). The blank part in the middle of the line should have "Kestrel Wellness", and in smaller writing below, "The Tension Fix".
• Bottom right corner should have the contact and business details.
• On the back we'd like a "next appointment" and "refer a friend" option.
Nice to have
• Matt finish - no gloss
• If you have a design which doesn't fit the above, but you feel suits the business, please submit anyway - sometimes you don't know what you like until you see it.
Should not have
• Anything 'Zen'. The business promotes the physiological and scientific benefits of massage. For clients with spiritual or meditative needs, we refer out.

```html
<!DOCTYPE html>
<html lang="en">
<head>
<meta charset="utf-8">
<title>Kestrel Wellness – Business Card</title>
<link rel="stylesheet" href="https://fonts.googleapis.com/css2?family=Jost:wght@300;400;500;600&display=swap">
<style>
  :root {
    --green: #6a9a2a;
    --green-bright: #7cb02c;
    --green-deep: #3f6b14;
    --black: #000000;
    --steel: #a7a9ab;
    --charcoal: #5e6062;
    --paper: #ffffff;
    --ground: #ecebe8;
    --white-soft: #f1f1f1;
  }
  * { margin: 0; padding: 0; box-sizing: border-box; }
  html, body { width: 1200px; height: 800px; overflow: hidden; }
  body {
    background: var(--ground);
    font-family: "Jost", sans-serif;
    position: relative;
  }
  .card {
    position: absolute;
    left: 280px;
    width: 640px;
    height: 374px;
    overflow: hidden;
    box-shadow: 0 2px 8px rgba(0,0,0,0.18);
  }
  .card--front { top: 18px; background: var(--black); }
  .card--back { top: 408px; background: var(--paper); }

  /* Front */
  .anatomy-panel {
    position: absolute;
    left: 0; top: 0;
    width: 243px; height: 100%;
    background: var(--green);
  }
  .anatomy-figure {
    position: absolute;
    left: 0; top: 0;
    width: 220px; height: 100%;
    background: linear-gradient(160deg, #4d7f1c 0%, #5f9224 40%, #3e6a14 100%);
  }
  .tension-point {
    position: absolute;
    border-radius: 50%;
    background: rgba(255,255,255,0.35);
    border: 2px solid rgba(255,255,255,0.55);
  }
  .tension-point--neck { left: 66px; top: 30px; width: 50px; height: 50px; }
  .tension-point--lower-back { left: 63px; top: 275px; width: 74px; height: 74px; }

  .brand {
    position: absolute;
    left: 282px; top: 118px;
  }
  .brand__name {
    display: flex;
    align-items: center;
    gap: 10px;
    font-weight: 600;
    font-size: 29px;
    letter-spacing: 0.5px;
    text-transform: uppercase;
    color: var(--green-bright);
    line-height: 1;
  }
  .brand__dot {
    width: 12px; height: 12px;
    border-radius: 50%;
    background: var(--steel);
  }
  .brand__tagline {
    margin-top: 8px;
    margin-left: 22px;
    font-weight: 400;
    font-size: 20px;
    letter-spacing: 3px;
    text-transform: uppercase;
    color: var(--white-soft);
    line-height: 1;
  }

  .contact {
    position: absolute;
    right: 24px; bottom: 28px;
    text-align: right;
    font-weight: 300;
    color: var(--steel);
    line-height: 1.25;
  }
  .contact__name, .contact__role { font-size: 19px; }
  .contact__phone { font-size: 20px; letter-spacing: 1px; margin-top: 4px; }
  .contact__email { font-size: 19px; }

  /* Back */
  .anatomy-ghost {
    position: absolute;
    left: 0; top: 0;
    width: 255px; height: 100%;
    background: linear-gradient(90deg, #d9d9d9 0%, #e7e7e7 55%, #f7f7f7 92%, var(--paper) 100%);
  }
  .follow-up {
    position: absolute;
    left: 192px; right: 20px;
    top: 282px;
  }
  .follow-up__row {
    display: flex;
    align-items: flex-end;
    height: 40px;
  }
  .follow-up__label {
    font-weight: 500;
    font-size: 18px;
    letter-spacing: 1px;
    text-transform: uppercase;
    color: var(--charcoal);
    white-space: nowrap;
    line-height: 1;
  }
  .follow-up__line {
    flex: 1;
    border-bottom: 1px solid var(--charcoal);
    margin-left: 2px;
    margin-bottom: 2px;
  }
</style>
</head>
<body>

  <section class="card card--front" aria-label="Business card front">
    <div class="anatomy-panel">
      <div class="anatomy-figure" role="img" aria-label="Green-toned anatomical illustration of the back muscle system, seen from behind"></div>
      <span class="tension-point tension-point--neck"></span>
      <span class="tension-point tension-point--lower-back"></span>
    </div>

    <div class="brand">
      <div class="brand__name"><span class="brand__dot"></span>Kestrel Wellness</div>
      <div class="brand__tagline">The Tension Fix</div>
    </div>

    <div class="contact">
      <div class="contact__name">Marcus</div>
      <div class="contact__role">Massage Therapist</div>
      <div class="contact__phone">0458203617</div>
      <div class="contact__email">info@ktfbodywork.example</div>
    </div>
  </section>

  <section class="card card--back" aria-label="Business card back">
    <div class="anatomy-ghost" role="img" aria-label="Faint grey anatomical illustration of the back and shoulder muscles"></div>
    <div class="follow-up">
      <div class="follow-up__row">
        <span class="follow-up__label">Next Appointment</span>
        <span class="follow-up__line"></span>
      </div>
      <div class="follow-up__row">
        <span class="follow-up__label">Refer a Friend</span>
        <span class="follow-up__line"></span>
      </div>
    </div>
  </section>

</body>
</html>
```